New business card for a regional office of a US M&A company

We need business card for a finance company, office based in Hong Kong , our Head office is in US, our business is to Merge and acquires companies , the new office will be a regional office for the Asia Pacific region. We want to use the head office logo as attached ( but don't have to be exactly the same, can be a variation to it) as a base and then add Asia Pacific alongside the logo.
We would prefer to have be bilingual Eng + Chinese, although we don't really have Chinese company name .

Industry/Entity Type

Business

Contact Information for Business Card

Clara Ruth Lindqvist
 

VP,
APAC M&A Operations
Oran Meridian Asia Pacific Limited
 
Unit 1807, K28
14 Tai Lok Fung Road, 
Hong Kong 
 
M: +852 6418 2074
T : +852 2836 4100
F : +852 2836 4177
VOIP: 4815
 
crlindqvist@oranmeridian.com

Font styles to use
Serif
Sans Serif

Colors

Designer to choose colors to be used in the design.

Requirements
Must have
• APAC Office

```html
<!DOCTYPE html>
<html lang="en">
<head>
<meta charset="utf-8">
<title>Oran Meridian Asia Pacific – Business Card</title>
<link rel="stylesheet" href="https://fonts.googleapis.com/css2?family=Open+Sans:wght@400;600;700&display=swap">
<style>
  :root {
    --stage: #000000;
    --paper: #ffffff;
    --navy: #0f2a40;
    --navy-deep: #0c2335;
    --accent: #1fa3c9;
    --ink: #1d2b3a;
    --grey: #6d6e70;
  }
  * { margin: 0; padding: 0; box-sizing: border-box; }
  html, body { width: 1200px; height: 900px; overflow: hidden; background: var(--stage); }
  body { position: relative; font-family: "Open Sans", sans-serif; }

  .card { position: absolute; top: 275px; width: 477px; height: 293px; }
  .card-front { left: 116px; background: var(--paper); border-radius: 0 50px 0 50px; color: var(--ink); }
  .card-back { left: 622px; background: var(--navy); border-radius: 50px 0 50px 0; overflow: hidden; }

  .holder { position: absolute; left: 30px; top: 26px; }
  .holder-name { font-size: 17px; font-weight: 600; color: var(--accent); line-height: 1.2; }
  .holder-title { font-size: 12.5px; color: var(--ink); margin-top: 3px; }

  .brand { position: absolute; left: 30px; top: 90px; display: flex; align-items: center; gap: 12px; }
  .brand-mark { width: 62px; height: 62px; background: var(--navy); }
  .brand-name { color: var(--accent); font-weight: 700; line-height: 1.05; text-transform: uppercase; }
  .brand-name .line-1 { display: block; font-size: 24px; }
  .brand-name .line-2 { display: block; font-size: 18px; }

  .contacts { position: absolute; right: 18px; top: 129px; list-style: none; text-align: right; }
  .contacts li { font-size: 12.5px; line-height: 20px; display: flex; justify-content: flex-end; align-items: center; gap: 6px; }
  .contacts svg { width: 10px; height: 10px; fill: var(--accent); }
  .contacts .no-icon { padding-right: 16px; }

  .office { position: absolute; right: 18px; top: 235px; text-align: right; }
  .office-name { font-size: 13.5px; font-weight: 600; color: var(--accent); }
  .office-address { font-size: 12.5px; color: var(--ink); margin-top: 2px; }

  .back-tone { position: absolute; inset: 0; background: linear-gradient(110deg, var(--navy-deep) 0%, var(--navy) 55%); }
  .back-brand { position: absolute; right: 56px; bottom: 26px; color: var(--accent); font-weight: 700; line-height: 1.05; text-transform: uppercase; text-align: left; }
  .back-brand .line-1 { display: block; font-size: 24px; }
  .back-brand .line-2 { display: block; font-size: 18px; }
</style>
</head>
<body>
  <section class="card card-front">
    <div class="holder">
      <p class="holder-name">Clara Ruth Lindqvist VP,</p>
      <p class="holder-title">APAC M&amp;A Operations</p>
    </div>

    <div class="brand">
      <div class="brand-mark"></div>
      <p class="brand-name"><span class="line-1">Oran Meridian</span><span class="line-2">Asia Pacific Ltd</span></p>
    </div>

    <ul class="contacts">
      <li>+852 6418 2074
        <svg viewBox="0 0 10 10" aria-label="mobile"><path d="M2 0h6v10H2zM3 1v7h4V1z"/></svg></li>
      <li>+852 2836 4100
        <svg viewBox="0 0 10 10" aria-label="telephone"><path d="M2 0l2 2-1 1.5c.8 1.6 1.9 2.7 3.5 3.5L8 6l2 2-1.5 2C4 9.5.5 6 0 1.5z"/></svg></li>
      <li>+852 2836 4177
        <svg viewBox="0 0 10 10" aria-label="fax"><path d="M2 0h5v3H2zM0 3h10v7H0zM2 5h2v1H2zm4 0h2v1H6zM2 7h2v1H2zm4 0h2v1H6z"/></svg></li>
      <li>crlindqvist@oranmeridian.com
        <svg viewBox="0 0 10 10" aria-label="email"><path d="M0 2h10v6H0zM.8 2.6 5 5.6l4.2-3z" fill-rule="evenodd"/></svg></li>
      <li class="no-icon">VOIP: 4815</li>
    </ul>

    <div class="office">
      <p class="office-name">Oran Meridian Asia Pacific Ltd</p>
      <p class="office-address">Unit 1807, K28 14 Tai Lok Fung Road, Hong Kong</p>
    </div>
  </section>

  <section class="card card-back">
    <div class="back-tone"></div>
    <p class="back-brand"><span class="line-1">Oran Meridian</span><span class="line-2">Asia Pacific Ltd</span></p>
  </section>
</body>
</html>
```